Aircraft maintenance buisness card

I am an aircraft mechanic looking for a personal buisness card . I would like my name and a title of Aircraft Maintenance Manager . I would like a suttle picture of an aircraft and helicopter .

elegant and professional wtih my contact .

My name should be on the car and Aircraft Maintenance Manager under with my contact infor below .

i have attached some pictures but i am open to other pics and ideas . I would like a airliner or private jet and a helicopter in the picture . The Images should be suttle and not the main idea . I also uploaded a picture of a jet engine which is cool . Be creative and i will work with you to finalize something .
Updates

Project Deadline Extended
Reason: Looking for more variations . Very good so far but looiking for a bit more styles and i uploaded my logo that i purchased . Please use my logo and be creative with it . I like some variations of black card with maybe some pictures that i uploaded but i am open to ideas . Be creative and i will work with you .

Project Deadline Extended
Reason: Looking for more designs and variations . Not yet satisfied with the designs i have gotten .

Industry/Entity Type

Aviation

Contact Information for Business Card

Aircraft Maintenance Manager

Font styles to use
Serif

Colors

Designer to choose colors to be used in the design.

Requirements
Must have
• An aviation related Logo if possible incorporated in the card possibly
• My name
• Tiberio Malvade Furtunato
• 482 Pellow St.
• Brenmore , PA
• 08519
• Email: Lwskyfixtech@mailvora.com
Nice to have
• Suttle Backround of a Private Jet or Airliner and a Helicopter .

```html
<!DOCTYPE html>
<html lang="en">
<head>
<meta charset="utf-8">
<title>Skyfix Aviation – Business Card</title>
<link rel="stylesheet" href="https://fonts.googleapis.com/css2?family=Nunito:wght@700;800&family=Roboto:wght@400&display=swap">
<style>
  :root {
    --backdrop: #e6e6e6;
    --card-white: #f1f1f1;
    --card-black: #0b0b0c;
    --engine-dark: #1a1b1d;
    --engine-mid: #2a2b2e;
    --brand-blue: #1d46a8;
    --ink: #1b1b1b;
    --icon-ink: #333333;
    --logo-white: #ffffff;
  }
  * { margin: 0; padding: 0; box-sizing: border-box; }
  html, body { width: 1200px; height: 1000px; overflow: hidden; }
  body { background: var(--backdrop); position: relative; font-family: "Roboto", sans-serif; }

  .card { position: absolute; left: 305px; width: 590px; height: 338px; overflow: hidden; }
  .card-front { top: 130px; background: var(--card-black); }
  .card-back { top: 532px; background: var(--card-white); }

  .engine-photo {
    position: absolute; inset: 0;
    background: radial-gradient(ellipse at 85% 45%, var(--engine-mid) 0%, var(--engine-dark) 40%, var(--card-black) 80%);
  }

  .brand-mark { position: absolute; display: flex; align-items: center; color: var(--logo-white); font-family: "Nunito", sans-serif; font-weight: 800; white-space: nowrap; }
  .brand-dot { border-radius: 50%; background: var(--brand-blue); flex: none; }
  .brand-name { line-height: 1; letter-spacing: 1px; text-transform: uppercase; }

  .card-front .brand-mark { left: 205px; top: 148px; gap: 10px; }
  .card-front .brand-dot { width: 40px; height: 40px; }
  .card-front .brand-name { font-size: 22px; }

  .card-back .brand-mark { left: 410px; top: 136px; gap: 8px; }
  .card-back .brand-dot { width: 26px; height: 26px; background: var(--logo-white); }
  .card-back .brand-name { font-size: 14px; letter-spacing: 0.5px; }

  .back-art { position: absolute; inset: 0; }

  .contact-line { position: absolute; left: 30px; display: flex; align-items: flex-start; gap: 14px; font-size: 16.5px; color: var(--ink); line-height: 1.15; }
  .contact-line svg { flex: none; }
  .contact-address { top: 98px; }
  .contact-email { top: 161px; align-items: center; }

  .holder-name { position: absolute; left: 30px; top: 264px; font-family: "Nunito", sans-serif; font-weight: 800; font-size: 24px; color: var(--ink); }
  .holder-title { position: absolute; left: 30px; top: 294px; font-size: 16px; color: var(--brand-blue); }
</style>
</head>
<body>

<section class="card card-front">
  <div class="engine-photo" role="img" aria-label="Dark close-up photograph of jet engine fan blades"></div>
  <div class="brand-mark">
    <span class="brand-dot"></span>
    <span class="brand-name">Skyfix Aviation</span>
  </div>
</section>

<section class="card card-back">
  <svg class="back-art" width="590" height="338" viewBox="0 0 590 338">
    <polygon points="238,0 590,0 590,338 510,338 430,250 375,190" fill="#141517" role="img" aria-label="Dark photograph of jet engine fan blades"/>
    <polygon points="238,0 252,0 356,187 342,187" fill="var(--brand-blue)"/>
    <polygon points="262,0 278,0 330,95 314,95" fill="var(--brand-blue)"/>
    <polygon points="510,0 528,0 590,90 590,112" fill="var(--brand-blue)"/>
    <polygon points="425,262 470,262 518,338 474,338" fill="var(--brand-blue)"/>
  </svg>

  <div class="contact-line contact-address">
    <svg width="20" height="30" viewBox="0 0 20 30" aria-hidden="true">
      <path d="M10 2a8 8 0 0 0-8 8c0 6 8 17 8 17s8-11 8-17a8 8 0 0 0-8-8z" fill="none" stroke="var(--icon-ink)" stroke-width="2.2"/>
      <circle cx="10" cy="10" r="3" fill="var(--icon-ink)"/>
    </svg>
    <span>482 Pellow St.<br>Brenmore , PA &nbsp;08519</span>
  </div>

  <div class="contact-line contact-email">
    <svg width="24" height="18" viewBox="0 0 24 18" aria-hidden="true">
      <rect x="1" y="1" width="22" height="16" fill="none" stroke="var(--icon-ink)" stroke-width="1.8"/>
      <path d="M1 1l11 9 11-9M1 17l8-7M23 17l-8-7" fill="none" stroke="var(--icon-ink)" stroke-width="1.6"/>
    </svg>
    <span>Lwskyfixtech@mailvora.com</span>
  </div>

  <div class="brand-mark">
    <span class="brand-dot"></span>
    <span class="brand-name">Skyfix Aviation</span>
  </div>

  <h1 class="holder-name">Tiberio Malvade Furtunato</h1>
  <p class="holder-title">Aircraft Maintenance Manager</p>
</section>

</body>
</html>
```